Loan Company looking to offer special summer loan rate for closed customers

We are wanting to design an A5 Summer Holiday themed leaflet. We would like to offer a 10% Cashback when re-opening their loan account.
The leaflet is aimed at our closed customers. We would like to use bright summer colours. I have uploaded one of our Christmas promotion leaflets for you to include the highlighted information to use in this new project. We have also uploaded some ideas of examples that we have seen online as rough guide.
"10% Cashback on all re-opened accounts in July and August 2023!"

```html
<!DOCTYPE html>
<html lang="en">
<head>
<meta charset="utf-8">
<title>Sapphire Financial Services – Summer Cashback</title>
<link rel="stylesheet" href="https://fonts.googleapis.com/css2?family=Rubik:ital,wght@0,700;0,900;1,900&family=Lexend:wght@400;600&display=swap">
<style>
  :root {
    --sea-teal: #0a8789;
    --sky-teal: #2a9a9c;
    --sand: #ddd3a8;
    --sand-light: #e6dcb4;
    --band-blue: #2185a6;
    --promo-red: #f23347;
    --promo-red-dark: #c9182d;
    --off-white: #f2e8e2;
    --ink: #1d1d1b;
    --white: #ffffff;
  }
  * { margin: 0; padding: 0; box-sizing: border-box; }
  html, body { width: 846px; height: 1200px; overflow: hidden; }
  body { font-family: "Lexend", sans-serif; color: var(--ink); }

  .leaflet { position: relative; width: 846px; height: 1200px; overflow: hidden; }

  .beach-scene {
    position: absolute; inset: 0;
    background: linear-gradient(180deg,
      var(--sea-teal) 0%, var(--sky-teal) 30%, #4aa9a8 52%,
      #3c9e9e 62%, #a9c7b0 70%, var(--sand-light) 78%, var(--sand) 100%);
  }

  .brand {
    position: absolute; left: 0; right: 0; top: 170px;
    text-align: center; color: var(--white);
    font-family: "Rubik", sans-serif; font-weight: 700;
  }
  .brand-name { font-size: 58px; letter-spacing: 2px; line-height: 1; }
  .brand-band {
    position: absolute; left: 198px; top: 88px; width: 450px; height: 58px;
    background: var(--band-blue); opacity: 0.85;
  }
  .brand-line { position: relative; }
  .brand-services { font-size: 33px; margin-top: 10px; line-height: 1.1; }
  .brand-region { font-size: 18px; letter-spacing: 5px; margin-top: 6px; padding-left: 10px; }

  .offer-figure {
    position: absolute; left: 236px; top: 470px; width: 400px;
    font-family: "Rubik", sans-serif; font-weight: 900;
    color: var(--promo-red); font-size: 215px; line-height: 1; letter-spacing: -8px;
    text-shadow: 4px 4px 0 var(--promo-red-dark);
  }
  .offer-figure .percent { font-size: 118px; letter-spacing: 0; }

  .offer-block {
    position: absolute; left: 207px; top: 654px; width: 426px; height: 153px;
    background: linear-gradient(180deg, var(--promo-red) 0%, #ec1f3c 100%);
    box-shadow: 0 4px 0 var(--promo-red-dark);
    display: flex; align-items: center; justify-content: center;
    font-family: "Rubik", sans-serif; font-weight: 900;
    font-size: 128px; color: var(--off-white); letter-spacing: -2px;
    text-shadow: 3px 3px 0 #b9aaa4;
  }

  .offer-headline {
    position: absolute; left: 0; right: 0; top: 826px; text-align: center;
    font-family: "Rubik", sans-serif; font-weight: 900; font-style: italic;
    font-size: 18.5px; line-height: 21px; color: var(--promo-red);
    text-shadow: 1px 1px 0 var(--white), -1px -1px 0 var(--white), 1px -1px 0 var(--white), -1px 1px 0 var(--white);
  }

  .call-pill {
    position: absolute; left: 252px; top: 906px; width: 336px; height: 63px;
    background: #e8383f; border-radius: 32px;
    display: flex; align-items: center; padding: 0 6px;
  }
  .call-icon {
    width: 53px; height: 53px; border-radius: 50%; background: var(--white);
    display: flex; align-items: center; justify-content: center; flex: none;
  }
  .call-number {
    margin-left: 8px; flex: 1; height: 53px; border-radius: 27px; background: var(--white);
    display: flex; align-items: center; justify-content: center;
    font-family: "Rubik", sans-serif; font-weight: 900; font-style: italic;
    font-size: 26px; color: #e0323a; letter-spacing: 0.5px;
  }

  .legal {
    position: absolute; left: 120px; right: 120px; top: 985px;
    text-align: center; font-size: 15.6px; line-height: 21.6px;
  }
  .legal-title { font-weight: 600; }
  .legal-terms { margin-top: 21px; }
</style>
</head>
<body>
<main class="leaflet">
  <div class="beach-scene" role="img" aria-label="Illustrated summer beach with striped parasols, deck chairs, sea and clouds"></div>

  <header class="brand">
    <div class="brand-band"></div>
    <div class="brand-line brand-name">SAPPHIRE</div>
    <div class="brand-line brand-services">Financial Services</div>
    <div class="brand-line brand-region">(Pennine) Limited</div>
  </header>

  <div class="offer-figure">10<span class="percent">%</span></div>
  <div class="offer-block">OFF</div>

  <p class="offer-headline">CASHBACK ON ALL RE-OPENED ACCOUNTS<br>IN JULY AND AUGUST 2023!</p>

  <div class="call-pill">
    <div class="call-icon">
      <svg width="30" height="30" viewBox="0 0 24 24" aria-hidden="true">
        <path fill="#e0323a" d="M6.6 10.8a15.1 15.1 0 0 0 6.6 6.6l2.2-2.2a1 1 0 0 1 1-.25 11.4 11.4 0 0 0 3.6.57 1 1 0 0 1 1 1V20a1 1 0 0 1-1 1A17 17 0 0 1 3 4a1 1 0 0 1 1-1h3.5a1 1 0 0 1 1 1c0 1.25.2 2.45.57 3.57a1 1 0 0 1-.25 1z"/>
      </svg>
    </div>
    <div class="call-number">01632 960 482</div>
  </div>

  <section class="legal">
    <p class="legal-title">Representative example:</p>
    <p>Loan amount €150.00 payable over 23 weeks at £10.50 per week. Interest is £91.50 The Total amount payable is £241.50. Interest rate is 138.29% per annum (fixed). 838.39% APR representative.</p>
    <p class="legal-terms">Terms and conditions apply. All credit is subject to status &amp; affordability. Written quotations on request</p>
  </section>
</main>
</body>
</html>
```